Anzeigengestaltung für Steuerberatungsgesellschaft
Zielgruppe
Die KTR Steuerberatungsgesellschaft mbH zählt zu einer der führenden Steuerberatungsgesellschaften für mittelständische Unternehmen in Sachsen. Unabhängig, professionell und vertrauensvoll. Getreu unserem Leitbild 'Unternehmer beraten Unternehmer' werden Sie von einem konstanten Beratungsteam betreut, welches sich an den Standorten Görlitz und Dres-den um ALLE Ihre steuerlichen Fragen und Themen kümmert. Darüber hinaus verfügen unse-re Mitarbeiter über ein umfangreiches betriebswirtschaftliches Fachwissen und sind daher jederzeit in der Lage, Sie auch in angrenzenden Themen zu unterstützen.
Aufgabenstellung
Siehe Briefing (ppt)

```html
<!DOCTYPE html>
<html lang="de">
<head>
<meta charset="utf-8">
<title>KTR Steuerberatung – Stellenanzeige</title>
<link rel="stylesheet" href="https://fonts.googleapis.com/css2?family=Open+Sans:wght@400;600;700;800&display=swap">
<style>
  :root {
    --navy: #2b2d4e;
    --red: #c0272d;
    --white: #ffffff;
    --rule: #8a8a8a;
    --text-dark: #2a2c40;
    --sky-top: #b9cfe0;
    --sky-mid: #dfe7ee;
    --sea: #6f8ea6;
    --wall: #a89f88;
  }
  * { box-sizing: border-box; margin: 0; padding: 0; }
  html, body { width: 1200px; height: 1200px; overflow: hidden; background: var(--white); }
  body { position: relative; font-family: "Open Sans", sans-serif; }

  .brand-header {
    position: absolute; left: 0; top: 0; width: 1200px; height: 217px;
    border-bottom: 1px solid var(--rule);
    display: flex; flex-direction: column; align-items: center; justify-content: center;
    color: var(--navy); font-weight: 800; line-height: 1;
    padding-bottom: 20px;
  }
  .brand-header .brand-name { font-size: 84px; letter-spacing: 6px; }
  .brand-header .brand-sub { font-size: 20px; letter-spacing: 4px; margin-top: 6px; }

  .job-ad {
    position: absolute; left: 94px; top: 385px; width: 1012px; height: 529px;
    border: 1px solid #6c6c6c; overflow: hidden;
  }
  .ad-photo {
    position: absolute; inset: 0;
    background: linear-gradient(180deg, var(--sky-top) 0%, var(--sky-mid) 55%, #cfd9e1 76%, var(--sea) 80%, var(--sea) 83%, var(--wall) 85%, #8f8672 91%, var(--navy) 91%);
  }
  .headline {
    position: absolute; left: 32px; top: 33px; width: 502px; height: 76px;
    background: var(--navy); color: var(--white);
    font-size: 39px; font-weight: 700; line-height: 76px; padding-left: 18px; letter-spacing: 0.5px;
  }
  .callout {
    position: absolute; left: 34px; top: 119px; width: 363px; height: 60px;
    background: var(--red); color: var(--white);
    font-size: 40px; font-weight: 700; line-height: 60px; padding-left: 16px;
  }
  .positions {
    position: absolute; left: 34px; top: 196px;
    font-size: 19.5px; font-weight: 600; line-height: 28px; color: var(--text-dark);
  }
  .ad-brand {
    position: absolute; left: 797px; top: 31px; width: 190px; text-align: center;
    color: var(--navy); font-weight: 800; line-height: 1;
  }
  .ad-brand .brand-name { font-size: 46px; letter-spacing: 4px; }
  .ad-brand .brand-sub { font-size: 11px; letter-spacing: 2px; margin-top: 3px; }
  .badges { position: absolute; inset: 0; pointer-events: none; }
  .badge-text {
    position: absolute; color: var(--white); text-align: center; transform: translate(-50%, -50%);
  }
  .bonus { left: 892px; top: 176px; }
  .bonus .amount { font-size: 23px; font-weight: 700; display: block; }
  .bonus .label { font-size: 15px; font-weight: 400; display: block; margin-top: 6px; }
  .locations { left: 910px; top: 295px; font-size: 19px; font-weight: 700; line-height: 27px; }
  .apply-bar {
    position: absolute; left: 0; bottom: 0; width: 100%; height: 62px;
    background: var(--navy); color: var(--white);
    font-size: 19px; font-weight: 700; letter-spacing: 1px;
    display: flex; align-items: center; justify-content: center;
  }
</style>
</head>
<body>
  <header class="brand-header">
    <span class="brand-name">KTR</span>
    <span class="brand-sub">STEUERBERATUNG</span>
  </header>

  <section class="job-ad">
    <div class="ad-photo" role="img" aria-label="Foto: Menschen mit schwarzen Schirmen gehen auf einer Mauer am Meer, eine Person hebt mit rotem Schirm ab"></div>

    <h1 class="headline">BEREIT ZUM ABHEBEN?</h1>
    <h2 class="callout">Wir suchen dich!</h2>
    <p class="positions">Steuerfachangestellter &amp; Steuerfachwirt (m/w/d)<br>mit Kenntnissen PAYRIX LOHN</p>

    <div class="ad-brand">
      <div class="brand-name">KTR</div>
      <div class="brand-sub">STEUERBERATUNG</div>
    </div>

    <svg class="badges" width="1012" height="529" viewBox="0 0 1012 529" aria-hidden="true">
      <circle cx="910" cy="295" r="77" fill="var(--navy)"/>
      <polygon points="842,160 753,203 845,190" fill="var(--red)"/>
      <circle cx="892" cy="176" r="69" fill="var(--red)"/>
    </svg>
    <div class="badge-text bonus"><span class="amount">2.500 €</span><span class="label">Wechselprämie</span></div>
    <div class="badge-text locations">Dresden<br>Görlitz<br>Home-Office</div>

    <footer class="apply-bar">JETZT BEWERBEN: Jobhotline +49 3581 55 123 40</footer>
  </section>
</body>
</html>
```